IT Consulting, IT Beacon, Software Development, Network Solutions, Hosting

Attached is logo for our company, we just was the designers to come up with creative ideas to use the logo and the theme to come with creative and energetic business cards that leave an impression and stick in people's head.

Target Market(s)

Medical, Law, Entertainment, Real estate, any small to medium size business.

Industry/Entity Type

Business

Font styles to use
Serif
Sans Serif

```html
<!DOCTYPE html>
<html lang="en">
<head>
<meta charset="utf-8">
<title>IT Beacon Business Cards</title>
<link rel="stylesheet" href="https://fonts.googleapis.com/css2?family=Questrial&display=swap">
<style>
  :root {
    --canvas-bg: #f4f4f4;
    --card-white: #ffffff;
    --card-shade: #eeeeee;
    --card-dark: #141b1e;
    --accent-yellow: #f7cb0f;
    --ink: #1c1f22;
    --ink-soft: #3a3d40;
  }
  * { box-sizing: border-box; margin: 0; padding: 0; }
  html, body { width: 1200px; height: 900px; overflow: hidden; }
  body {
    background: var(--canvas-bg);
    font-family: "Questrial", "Helvetica Neue", Arial, sans-serif;
    position: relative;
  }
  .card {
    position: absolute;
    top: 300px;
    width: 520px;
    height: 300px;
    border-radius: 24px;
    overflow: hidden;
    box-shadow: 0 10px 28px rgba(0,0,0,0.14);
  }
  .card-front {
    left: 60px;
    background: linear-gradient(180deg, var(--card-shade) 0%, var(--card-white) 45%);
  }
  .card-back {
    left: 620px;
    background: var(--card-dark);
    display: flex;
    align-items: center;
    justify-content: center;
  }
  .wordmark {
    letter-spacing: 1px;
    line-height: 1;
    white-space: nowrap;
  }
  .card-front .wordmark {
    position: absolute;
    left: 26px;
    top: 46px;
    font-size: 40px;
    color: var(--ink);
  }
  .card-back .wordmark {
    font-size: 60px;
    letter-spacing: 3px;
    color: var(--accent-yellow);
  }
  .holder {
    position: absolute;
    left: 26px;
    top: 128px;
  }
  .holder-name {
    font-size: 17px;
    font-weight: 700;
    color: var(--accent-yellow);
  }
  .holder-role {
    font-size: 11px;
    color: var(--ink-soft);
    margin-top: 2px;
  }
  .contact-list {
    position: absolute;
    left: 24px;
    top: 180px;
    list-style: none;
    font-size: 15px;
    color: var(--ink);
  }
  .contact-item {
    display: flex;
    align-items: flex-start;
    gap: 5px;
    line-height: 21px;
  }
  .contact-icon {
    width: 15px;
    height: 15px;
    margin-top: 2px;
    flex: none;
    fill: var(--accent-yellow);
    stroke: var(--accent-yellow);
  }
  .contact-address { display: flex; flex-direction: column; }
  .footer-band {
    position: absolute;
    left: 0;
    right: 0;
    bottom: 0;
    height: 34px;
    background: var(--card-dark);
    border-top: 4px solid var(--accent-yellow);
  }
</style>
</head>
<body>

  <section class="card card-front" aria-label="Business card front">
    <div class="wordmark">IT BEACON</div>

    <div class="holder">
      <div class="holder-name">Dana Whitfield</div>
      <div class="holder-role">Manager</div>
    </div>

    <ul class="contact-list">
      <li class="contact-item">
        <svg class="contact-icon" viewBox="0 0 16 16" aria-hidden="true"><path stroke="none" d="M3.2 1.2l2.4 0.2 1.2 3.1-1.6 1.3c0.9 1.9 2.2 3.2 4.1 4.1l1.3-1.6 3.1 1.2 0.2 2.4c-0.2 1.2-1.2 2.1-2.4 2-5.3-0.6-9.4-4.7-10-10C1.1 2.4 2 1.4 3.2 1.2z"/></svg>
        <span>1800-555-0142</span>
      </li>
      <li class="contact-item">
        <svg class="contact-icon" viewBox="0 0 16 16" aria-hidden="true"><rect x="1" y="3.5" width="14" height="10" rx="1" fill="none" stroke-width="1.6"/><path d="M1.5 4l6.5 5 6.5-5" fill="none" stroke-width="1.6"/></svg>
        <span>info@itbeacon.com</span>
      </li>
      <li class="contact-item">
        <svg class="contact-icon" viewBox="0 0 16 16" aria-hidden="true" fill="none"><circle cx="8" cy="8" r="6.5" fill="none" stroke-width="1.4"/><ellipse cx="8" cy="8" rx="2.8" ry="6.5" fill="none" stroke-width="1.2"/><path d="M1.5 8h13M2.5 4.8h11M2.5 11.2h11" fill="none" stroke-width="1.1"/></svg>
        <span>www.itbeacon.com</span>
      </li>
      <li class="contact-item">
        <svg class="contact-icon" viewBox="0 0 16 16" aria-hidden="true"><path stroke="none" d="M8 1.5l7 6.2-1 1.1-1-0.9V14.5H9.5v-4h-3v4H3V7.9l-1 0.9-1-1.1z"/></svg>
        <span class="contact-address">
          <span>1250 Harbor Ave. Suite 410</span>
          <span>Bay Harbor, FL 33154</span>
        </span>
      </li>
    </ul>

    <div class="footer-band"></div>
  </section>

  <section class="card card-back" aria-label="Business card back">
    <div class="wordmark">IT BEACON</div>
  </section>

</body>
</html>
```